UI/ UX Design for ERP Software

We need a new UX/UI interface for a ERP software for property managers. Our CMMS / ERP solution is made based on responsive design technologies and is coded in PHP.
The overall UX to be similar to Zel Kavo - easy navigation, intuitive menus.

Industry/Entity Type

Property Management

Number of Pages Required

5+ page

Requirements
Must have
• Round dock buttons
Consistent icons across the application
Enough Spacing between buttons/icons/ menu
Consistent Font
Nice to have
• We would like the UX to allow the users to use the application without /minimum training.
Should not have
• we don't want anything that is classic with respect to UX

```html
<!DOCTYPE html>
<html lang="en">
<head>
<meta charset="utf-8">
<title>Keystay – Dashboard</title>
<link href="https://fonts.googleapis.com/css2?family=Rubik:wght@400;500&family=Oswald:wght@300&display=swap" rel="stylesheet">
<style>
  :root {
    --brand: #1a7cf0;
    --ink: #2b2f36;
    --muted: #4a4f58;
    --label: #5a6372;
    --header-bg: #f7f8fa;
    --body-bg: #eef0f4;
    --card-bg: #ffffff;
    --line: #dde1e7;
    --footer-bg: #51627a;
    --faint: #e6e8ec;
    --users: #1a82fb;
    --properties: #e06262;
    --maintenance: #5ea5dc;
    --orders: #2035d0;
    --reports: #c061e0;
    --files: #8048f0;
    --pages: #8a6a3f;
    --config: #e9b500;
    --requests: #dd9a5e;
    --settings: #22c55e;
  }
  * { box-sizing: border-box; margin: 0; padding: 0; }
  html, body { width: 1200px; height: 669px; overflow: hidden; }
  body {
    position: relative;
    font-family: "Rubik", sans-serif;
    background: var(--body-bg);
    color: var(--ink);
  }
  .app-header {
    position: absolute; left: 0; top: 0; width: 1200px; height: 144px;
    background: var(--header-bg);
    border-bottom: 1px solid var(--line);
  }
  .brand {
    position: absolute; left: 34px; top: 14px;
    display: flex; align-items: center; gap: 8px;
    font-size: 30px; font-weight: 500; color: var(--brand);
  }
  .brand-mark { width: 22px; height: 22px; background: var(--brand); border-radius: 4px; }
  .welcome {
    position: absolute; left: 264px; top: 22px;
    font-size: 12px; color: var(--ink);
  }
  .welcome span { color: var(--brand); }
  .search {
    position: absolute; left: 498px; top: 15px; width: 329px; height: 30px;
    background: #fff; border: 1px solid #e5e8ec; border-radius: 15px;
    display: flex; align-items: center; justify-content: space-between;
    padding: 0 12px 0 20px; font-size: 10px; color: var(--muted);
  }
  .user {
    position: absolute; left: 966px; top: 16px;
    display: flex; align-items: center; gap: 8px;
    font-size: 12px; color: var(--muted);
  }
  .avatar { width: 28px; height: 28px; border-radius: 50%; background: linear-gradient(135deg,#c9a48a,#6d5a52); }
  .user b { font-weight: 400; color: var(--ink); }
  .power { position: absolute; left: 1157px; top: 23px; }
  .stat {
    position: absolute; top: 71px; width: 204px; height: 52px;
    background: var(--card-bg); border-radius: 2px; overflow: hidden;
    padding: 8px 14px;
  }
  .stat-label { font-size: 11px; color: var(--muted); }
  .stat-value {
    font-family: "Oswald", sans-serif; font-weight: 300;
    font-size: 20px; line-height: 24px; color: var(--brand); letter-spacing: -0.3px;
  }
  .stat svg { position: absolute; right: 0; top: 18px; }
  .modules { position: absolute; left: 14px; top: 170px; }
  .tile {
    position: absolute; width: 234px; height: 140px;
    display: flex; flex-direction: column; align-items: center;
  }
  .tile-icon {
    width: 60px; height: 60px; border-radius: 5px; margin-top: 22px;
    display: flex; align-items: center; justify-content: center;
    box-shadow: 0 6px 14px rgba(0,0,0,0.12);
  }
  .tile-name { margin-top: 13px; font-size: 13px; font-weight: 500; color: var(--muted); letter-spacing: 0.2px; }
  .app-footer {
    position: absolute; left: 0; top: 639px; width: 1200px; height: 30px;
    background: var(--footer-bg); color: #fff; font-size: 11px;
    padding: 8px 29px; letter-spacing: 0.3px;
  }
  svg.ic { fill: none; stroke: #fff; stroke-width: 1.4; stroke-linecap: round; stroke-linejoin: round; }
</style>
</head>
<body>
<header class="app-header">
  <div class="brand"><div class="brand-mark"></div>Keystay</div>
  <p class="welcome">Welcome to <span>Keystay</span></p>
  <div class="search">Search Asset ...
    <svg width="12" height="12" viewBox="0 0 12 12" fill="none" stroke="#a0a6b0" stroke-width="1.5"><circle cx="5" cy="5" r="3.8"/><path d="M8 8l3 3"/></svg>
  </div>
  <div class="user">
    <div class="avatar" role="img" aria-label="User profile photo"></div>
    <span>Welcome <b>Dana</b></span>
    <svg width="10" height="10" viewBox="0 0 10 10" fill="none" stroke="#2b2f36" stroke-width="1.6"><path d="M2 3.5l3 3 3-3"/></svg>
  </div>
  <svg class="power" width="14" height="14" viewBox="0 0 14 14" fill="none" stroke="#2b2f36" stroke-width="1.8" stroke-linecap="round"><path d="M7 1.5v5"/><path d="M4 3.5a4.5 4.5 0 1 0 6 0"/></svg>

  <div class="stat" style="left:30px">
    <div class="stat-label">Properties</div><div class="stat-value">03</div>
    <svg width="42" height="34" viewBox="0 0 42 34" fill="var(--faint)"><path d="M2 18L22 2l20 16h-6v16H8V18z"/></svg>
  </div>
  <div class="stat" style="left:264px">
    <div class="stat-label">Tenants</div><div class="stat-value">08</div>
    <svg width="44" height="34" viewBox="0 0 44 34" fill="var(--faint)"><circle cx="22" cy="8" r="7"/><circle cx="8" cy="12" r="5"/><circle cx="36" cy="12" r="5"/><path d="M10 34c0-10 6-16 12-16s12 6 12 16z"/><path d="M0 34c0-8 4-12 8-12s6 2 6 4v8zM44 34c0-8-4-12-8-12s-6 2-6 4v8z"/></svg>
  </div>
  <div class="stat" style="left:498px">
    <div class="stat-label">Total Properties Area</div><div class="stat-value">422,000.00 SQ.FT.</div>
    <svg width="32" height="32" viewBox="0 0 32 32" fill="none" stroke="var(--faint)" stroke-width="6"><path d="M3 12V3h9M20 3h9v9M29 20v9h-9M12 29H3v-9"/></svg>
  </div>
  <div class="stat" style="left:732px">
    <div class="stat-label">Rented Area</div><div class="stat-value">233,500.00 SQ.FT.</div>
    <svg width="32" height="32" viewBox="0 0 32 32" fill="none" stroke="var(--faint)" stroke-width="5"><path d="M3 12V3h9M20 3h9v9M29 20v9h-9M12 29H3v-9M8 8l16 16M24 8L8 24"/></svg>
  </div>
  <div class="stat" style="left:966px">
    <div class="stat-label">Vacancies Area</div><div class="stat-value">188,500.00</div>
    <svg width="32" height="32" viewBox="0 0 32 32" fill="none" stroke="var(--faint)" stroke-width="6"><path d="M3 12V3h9M20 3h9v9M29 20v9h-9M12 29H3v-9"/></svg>
  </div>
</header>

<main class="modules">
  <div class="tile" style="left:0;top:0">
    <div class="tile-icon" style="background:var(--users)"><svg class="ic" width="36" height="36" viewBox="0 0 36 36"><circle cx="18" cy="11" r="5"/><circle cx="8" cy="13" r="3.5"/><circle cx="28" cy="13" r="3.5"/><path d="M9 28c0-6 4-10 9-10s9 4 9 10z"/><path d="M2 26c0-4 2.5-7 6-7M34 26c0-4-2.5-7-6-7"/></svg></div>
    <div class="tile-name">Users</div>
  </div>
  <div class="tile" style="left:234px;top:0">
    <div class="tile-icon" style="background:var(--properties)"><svg class="ic" width="36" height="36" viewBox="0 0 36 36"><rect x="10" y="5" width="16" height="26"/><path d="M13 9h3M20 9h3M13 14h3M20 14h3M13 19h3M20 19h3M16 31v-6h4v6M4 31h28M6 31v-6M30 31v-6"/><circle cx="6" cy="22" r="2.5"/><circle cx="30" cy="22" r="2.5"/></svg></div>
    <div class="tile-name">Properties</div>
  </div>
  <div class="tile" style="left:468px;top:0">
    <div class="tile-icon" style="background:var(--maintenance)"><svg class="ic" width="36" height="36" viewBox="0 0 36 36"><path d="M12 11a6 6 0 0 1 12 0M10 11h16"/><circle cx="14" cy="24" r="6"/><circle cx="14" cy="24" r="2"/><circle cx="27" cy="21" r="3.5"/></svg></div>
    <div class="tile-name">Prevent. Maintenance</div>
  </div>
  <div class="tile" style="left:702px;top:0">
    <div class="tile-icon" style="background:var(--orders)"><svg class="ic" width="36" height="36" viewBox="0 0 36 36"><rect x="7" y="4" width="18" height="24" rx="1"/><path d="M11 10h10M11 15h8M11 20h5"/><path d="M20 32v-9a2 2 0 0 1 4 0v4h3a3 3 0 0 1 3 3v2"/></svg></div>
    <div class="tile-name">Orders</div>
  </div>
  <div class="tile" style="left:936px;top:0">
    <div class="tile-icon" style="background:var(--reports)"><svg class="ic" width="36" height="36" viewBox="0 0 36 36"><rect x="8" y="4" width="20" height="28" rx="1"/><path d="M11 10l1.5 1.5L15 9M17 10h8M11 16l1.5 1.5L15 15M17 16h8M11 22l1.5 1.5L15 21M17 22h8"/></svg></div>
    <div class="tile-name">Reports</div>
  </div>

  <div class="tile" style="left:0;top:158px">
    <div class="tile-icon" style="background:var(--files)"><svg class="ic" width="36" height="36" viewBox="0 0 36 36"><rect x="12" y="5" width="18" height="24" rx="1"/><path d="M12 9l-5 2 6 20 13-3M16 11h10M16 15h10M16 19h10M16 23h7"/></svg></div>
    <div class="tile-name">Files</div>
  </div>
  <div class="tile" style="left:234px;top:158px">
    <div class="tile-icon" style="background:var(--pages)"><svg class="ic" width="36" height="36" viewBox="0 0 36 36"><rect x="5" y="6" width="24" height="22" rx="1"/><path d="M5 11h24M8 8.5h1M11 8.5h1M9 16h8M9 20h6M9 24h8"/><rect x="19" y="17" width="12" height="10" rx="1"/><path d="M22 22h6"/></svg></div>
    <div class="tile-name">Pages</div>
  </div>
  <div class="tile" style="left:468px;top:158px">
    <div class="tile-icon" style="background:var(--config)"><svg class="ic" width="36" height="36" viewBox="0 0 36 36"><circle cx="18" cy="18" r="3.5"/><rect x="5" y="27" width="4" height="4"/><rect x="27" y="5" width="4" height="4"/><rect x="5" y="5" width="4" height="4"/><rect x="27" y="27" width="4" height="4"/><path d="M9 7h10v8M21 18h8v9M15 18H7v9M18 21v8h9M29 9v5"/></svg></div>
    <div class="tile-name">Configurations</div>
  </div>
  <div class="tile" style="left:702px;top:158px">
    <div class="tile-icon" style="background:var(--requests)"><svg class="ic" width="36" height="36" viewBox="0 0 36 36"><path d="M4 15v16h28V15L18 5z"/><path d="M4 31l11-9M32 31l-11-9M4 15l14 10 14-10"/><rect x="11" y="8" width="14" height="12"/><path d="M16 12a2 2 0 1 1 2 2v1.5M18 17.5v.2"/></svg></div>
    <div class="tile-name">Tenant Requests</div>
  </div>
  <div class="tile" style="left:936px;top:158px">
    <div class="tile-icon" style="background:var(--settings)"><svg class="ic" width="36" height="36" viewBox="0 0 36 36"><circle cx="18" cy="10" r="5"/><circle cx="18" cy="10" r="2"/><circle cx="9" cy="21" r="5"/><circle cx="9" cy="21" r="2"/><circle cx="25" cy="24" r="7"/><path d="M22 24h.1M25 24h.1M28 24h.1"/></svg></div>
    <div class="tile-name">Settings</div>
  </div>
</main>

<footer class="app-footer">© 2021 Keystay. All Rights Reserved</footer>
</body>
</html>
```